Public Speaking Book for aspiring, ambitious speakers

I'm looking for a 6x9 book cover (Parcelo standard) as well as ebook and audiobook formats.

I'm looking for orange font on a white background as these are my brand colours.

Feel free to use some yellow and gold too if you deem it appropriate.

Title: Climb and Glow
Subtitle: Find Your Voice. Tell Your Story. Share your Message.
Author: Lionel Barstow

I would like to have a picture of a female speaker on the front cover.

Alternatively, some kind of image that symbolises public speaking like a microphone, podium etc

Target Market(s)

Aspiring professional speakers

Colors
f78f20

Requirements
Must have
• Correct spelling!
Nice to have
• A logo or picture that fits the theme, but no pressure if you can't think of anything
Should not have
• No men in suits please. I don't want this to have a 1980s corporate look.

```html
<!DOCTYPE html>
<html lang="en">
<head>
<meta charset="utf-8">
<title>Climb and Glow — Lionel Barstow</title>
<link rel="stylesheet" href="https://fonts.googleapis.com/css2?family=Bebas+Neue&family=Open+Sans:wght@600&display=swap">
<style>
  :root {
    --cover-orange: #f78f20;
    --ink: #1d1d1b;
  }
  html, body {
    margin: 0;
    padding: 0;
    width: 800px;
    height: 1200px;
    overflow: hidden;
    background: var(--cover-orange);
  }
  .cover {
    position: relative;
    width: 800px;
    height: 1200px;
    background: var(--cover-orange);
    color: var(--ink);
    overflow: hidden;
  }
  .rule {
    position: absolute;
    height: 23px;
    background: var(--ink);
  }
  .rule--left { left: 0; width: 276px; border-radius: 0 4px 4px 0; }
  .rule--right { left: 516px; width: 284px; border-radius: 4px 0 0 4px; }
  .rule--top { top: 89px; }
  .rule--bottom { top: 1107px; }
  .quote-mark {
    position: absolute;
    left: 333px;
    width: 130px;
    height: 112px;
  }
  .quote-mark--open { top: 32px; }
  .quote-mark--close { top: 1066px; }
  .quote-mark path, .quote-mark circle { fill: var(--ink); }
  .title {
    margin: 0;
    font-weight: 400;
  }
  .title span, .subtitle, .author {
    position: absolute;
    left: 0;
    width: 800px;
    text-align: center;
    line-height: 1;
    white-space: nowrap;
  }
  .title span { font-family: "Bebas Neue", sans-serif; }
  .title__main { top: 171px; font-size: 375px; }
  .title__join { top: 476px; font-size: 112px; }
  .title__second { top: 567px; font-size: 210px; }
  .subtitle {
    top: 780px;
    margin: 0;
    font-family: "Bebas Neue", sans-serif;
    font-size: 37px;
    font-weight: 400;
  }
  .author {
    top: 986px;
    margin: 0;
    font-family: "Open Sans", sans-serif;
    font-weight: 600;
    font-size: 52px;
    letter-spacing: 1px;
  }
</style>
</head>
<body>
<main class="cover">
  <div class="rule rule--left rule--top"></div>
  <div class="rule rule--right rule--top"></div>

  <svg class="quote-mark quote-mark--open" viewBox="0 0 130 112" aria-hidden="true">
    <g>
      <circle cx="29" cy="83" r="29"/>
      <path d="M0.5,86 C-2,40 18,12 50,1 C56,-1 60,6 55,10 C40,20 31,34 29,54 L0.5,86 Z"/>
    </g>
    <g transform="translate(71 0)">
      <circle cx="29" cy="83" r="29"/>
      <path d="M0.5,86 C-2,40 18,12 50,1 C56,-1 60,6 55,10 C40,20 31,34 29,54 L0.5,86 Z"/>
    </g>
  </svg>

  <h1 class="title">
    <span class="title__main">Climb</span>
    <span class="title__join">And</span>
    <span class="title__second">Glow</span>
  </h1>

  <p class="subtitle">Find Your Voice. Tell Your Story. Share your Message.</p>

  <p class="author">Lionel Barstow</p>

  <svg class="quote-mark quote-mark--close" viewBox="0 0 130 112" aria-hidden="true">
    <g transform="rotate(180 65 56)">
      <g>
        <circle cx="29" cy="83" r="29"/>
        <path d="M0.5,86 C-2,40 18,12 50,1 C56,-1 60,6 55,10 C40,20 31,34 29,54 L0.5,86 Z"/>
      </g>
      <g transform="translate(71 0)">
        <circle cx="29" cy="83" r="29"/>
        <path d="M0.5,86 C-2,40 18,12 50,1 C56,-1 60,6 55,10 C40,20 31,34 29,54 L0.5,86 Z"/>
      </g>
    </g>
  </svg>

  <div class="rule rule--left rule--bottom"></div>
  <div class="rule rule--right rule--bottom"></div>
</main>
</body>
</html>
```